Candle Box & Belly Band Design

Design Candle Box for Soy Candles along with a belly band design that can be used on off the shelf coloured boxes. It is for a premium brand of candle - so i want the packaging to reflect this. I have included must haves below.

The candle boxes will be a few different sizes, but for the purpose of the design it would be something like a cube 12 x 12 x 12 cms

The belly band for standard boxes to be something like 5cm wide on a 12 x 12 x 12cms cube box that goes all the way around the top to the bottom - holding the lid on and providing all the relevant information. Example of box with belly band uploaded

Our company Name : Fern & Isla - our logo is uploaded

Target Market(s)

Premium Candle Buyers

Colors

Designer to choose colors to be used in the design.

Requirements
Must have
• Must have our logo - our logo can be in any colour
• Must state:
• Soy Candle, Hand Poured, Made in Melbourne,
• A space for the fragrance, size and burn time.
• For this project use Lime, Coconut & Elderfllower, 300grams, 50 Hour burn Time

```html
<!DOCTYPE html>
<html lang="en">
<head>
<meta charset="utf-8">
<title>Fern &amp; Isla Soy Candle Box</title>
<link href="https://fonts.googleapis.com/css2?family=Cinzel:wght@400;500&display=swap" rel="stylesheet">
<style>
  :root {
    --bg: #1a0507;
    --maroon-deep: #2a050b;
    --maroon: #4a0b15;
    --maroon-mid: #3a0710;
    --gold: #d9a53a;
    --gold-light: #f0c862;
    --gold-dark: #b07a22;
    --blush: #d98a96;
  }
  * { margin: 0; padding: 0; box-sizing: border-box; }
  html, body {
    width: 920px; height: 1200px; overflow: hidden;
    background: var(--bg);
    font-family: "Cinzel", "Times New Roman", serif;
  }
  .canvas {
    position: relative; width: 920px; height: 1200px;
    display: flex; flex-direction: column; align-items: center;
    justify-content: center; gap: 30px;
  }
  .panel {
    position: relative; width: 540px;
    overflow: hidden;
  }
  .lid-top {
    height: 500px;
    background: radial-gradient(ellipse at 55% 45%, var(--maroon) 0%, var(--maroon-mid) 45%, var(--maroon-deep) 100%);
    display: flex; align-items: center; justify-content: center;
  }
  .brand {
    display: flex; align-items: center; gap: 16px;
    color: var(--gold); font-size: 42px; font-weight: 500; letter-spacing: 2px;
  }
  .brand-dot {
    width: 22px; height: 22px; border-radius: 50%; background: var(--gold);
  }
  .box-front {
    height: 600px;
    background: linear-gradient(90deg, var(--maroon-mid), var(--maroon-deep));
  }
  .pattern {
    position: absolute; top: 0; bottom: 0; width: 150px;
    background: linear-gradient(180deg, #3b0811 0%, #4a0d17 50%, #32060d 100%);
  }
  .pattern-left { left: 0; }
  .pattern-right { right: 0; }
  .belly-band {
    position: absolute; top: 0; bottom: 0; left: 150px; width: 240px;
    background: linear-gradient(180deg, #2d050b 0%, #4c0a15 55%, #3a0710 100%);
    text-align: center;
  }
  .band-stripe {
    position: absolute; top: 0; bottom: 0; width: 10px;
    background: linear-gradient(180deg, var(--gold-dark), var(--gold-light) 40%, var(--gold) 70%, var(--gold-dark));
  }
  .band-stripe-left { left: 0; }
  .band-stripe-right { right: 0; }
  .product-title {
    margin-top: 78px; color: var(--gold);
    font-weight: 400; line-height: 1; 
  }
  .product-title .line-soy { display: block; font-size: 48px; }
  .product-title .line-candle { display: block; font-size: 50px; margin-top: 4px; }
  .title-rule {
    width: 170px; height: 2px; margin: 8px auto 8px; background: var(--gold);
  }
  .fragrance {
    color: var(--blush); font-size: 19px; line-height: 1.25;
  }
  .features { margin-top: 36px; color: var(--blush); font-size: 23px; line-height: 1.15; }
  .features p + p { margin-top: 22px; }
  .weight {
    position: absolute; right: 30px; bottom: 30px;
    color: var(--gold); font-size: 18px;
  }
</style>
</head>
<body>
<main class="canvas">
  <section class="panel lid-top">
    <div class="brand"><span class="brand-dot"></span><span>Fern &amp; Isla</span></div>
  </section>

  <section class="panel box-front">
    <div class="pattern pattern-left" role="img" aria-label="Faint tonal mandala flower pattern in deep red"></div>
    <div class="pattern pattern-right" role="img" aria-label="Faint tonal mandala flower pattern in deep red"></div>

    <div class="belly-band">
      <span class="band-stripe band-stripe-left"></span>
      <span class="band-stripe band-stripe-right"></span>

      <h1 class="product-title">
        <span class="line-soy">Soy</span>
        <span class="line-candle">Candle</span>
      </h1>
      <div class="title-rule"></div>
      <p class="fragrance">Lime - Coconut<br>Elderflower</p>

      <div class="features">
        <p>Hand Poured</p>
        <p>50 Hour<br>Burn Time</p>
        <p>Made in<br>Melbourne</p>
      </div>

      <p class="weight">300 gr</p>
    </div>
  </section>
</main>
</body>
</html>
```